Regional health service needs a PowerPoint design

We are a new organisation responsible for the purchasing of health services for the population of Marrowfield and Kelton in Essex, UK - a population of c.300,000.

We are looking for a set of powerpoint master slides for use principally as 'talk books' and reports for presenting information regarding the performance of the organisation externally and to use as the basis for producing internal reports and communications.

We would like to see designs which portray the organisation as being new and different from historic CHW organisations, whilst following the principles outlined within National CHW brand guidelines (see attached). The slides should communicate creativity and professionalism.

Our logo is available on request (due to technical issues, we cannot upload onto here).

Our brand guidelines are available at:
http://www.carewellmarks.example/all-guidelines/guidelines/authorised-clinical-commissioning-groups/introduction

An example report (which we would look to move over to our new template) is available at:
http://www.marrowfieldandkeltonhcb.example/key-documents/doc_download/142-integrated-plan-2013-15

Further information on us is available on our website: www.marrowfieldandkeltonhcb.example

Target Market(s)

Target audience is healthcare professionals and the general public.

Industry/Entity Type

Health

Requirements
Must have
• Include the organisations logo and provide a cover sheet front page and 3/4 slides showing how reports could be structured (e.g. narrative and graphical information / tabular information / use of photos etc).

Typefaces and colour schemes should be in line with our brand guidelines (i.e. principal use of Arial). Our guidelines are available at:

Nice to have
• As an organisation we are made up of four localities, it would be good to see designs that draw on this element of our organisation.

```html
<!DOCTYPE html>
<html lang="en">
<head>
<meta charset="utf-8">
<title>Integrated plan 2013-15 – Marrowfield and Kelton Clinical Commissioning Group</title>
<link href="https://fonts.googleapis.com/css2?family=Arimo:wght@400;700&display=swap" rel="stylesheet">
<style>
  :root {
    --page: #ffffff;
    --locality-blue: #0a8fcb;
    --locality-orange: #e28a05;
    --locality-green: #5bbf21;
    --locality-purple: #55038b;
    --locality-red: #d82006;
    --heading-blue: #2f80c2;
    --ink: #111111;
    --photo-light: #f1dde6;
    --photo-mid: #dcb6c6;
    --photo-warm: #c9a48f;
  }
  * { margin: 0; padding: 0; box-sizing: border-box; }
  html, body { width: 1200px; height: 900px; overflow: hidden; background: var(--page); }
  body { font-family: "Arimo", Arial, sans-serif; }

  .cover { position: relative; width: 1200px; height: 900px; background: var(--page); }

  .locality-bar { position: absolute; left: 37px; top: 30px; width: 111px; height: 548px; background: var(--locality-blue); }

  .cover-photo {
    position: absolute; left: 148px; top: 30px; width: 448px; height: 548px;
    background:
      radial-gradient(ellipse at 30% 55%, var(--photo-mid) 0%, transparent 55%),
      radial-gradient(ellipse at 75% 60%, var(--photo-warm) 0%, transparent 50%),
      linear-gradient(180deg, var(--photo-light) 0%, #ead0dc 60%, #e4c4d2 100%);
  }

  .tile { position: absolute; width: 270px; height: 267px; }
  .tile--orange { left: 607px; top: 30px; background: var(--locality-orange); }
  .tile--green  { left: 893px; top: 30px; width: 269px; background: var(--locality-green); }
  .tile--purple { left: 607px; top: 312px; height: 266px; background: var(--locality-purple); }
  .tile--red    { left: 893px; top: 312px; width: 269px; height: 266px; background: var(--locality-red); }

  .cover-title {
    position: absolute; left: 40px; top: 596px;
    font-size: 40px; font-weight: 700; color: var(--heading-blue); letter-spacing: 0.2px;
  }
  .cover-subtitle {
    position: absolute; left: 41px; top: 738px;
    font-size: 26px; font-weight: 700; line-height: 40px; color: var(--heading-blue);
  }

  .org-mark { position: absolute; right: 42px; top: 604px; text-align: right; }
  .org-mark__short {
    display: inline-block; font-size: 36px; font-weight: 700; color: var(--locality-blue);
    line-height: 42px; margin-bottom: 6px;
  }
  .org-mark__name {
    font-size: 30px; font-weight: 700; color: var(--ink); line-height: 42px;
  }
</style>
</head>
<body>
  <main class="cover">
    <div class="locality-bar"></div>
    <div class="cover-photo" role="img" aria-label="Photograph of a clinician listening to a young girl's chest with a stethoscope"></div>
    <div class="tile tile--orange"></div>
    <div class="tile tile--green"></div>
    <div class="tile tile--purple"></div>
    <div class="tile tile--red"></div>

    <h1 class="cover-title">Integrated plan 2013-15</h1>
    <p class="cover-subtitle">How the plan can work<br>across the four geographical areas</p>

    <div class="org-mark">
      <span class="org-mark__short">CHW</span>
      <p class="org-mark__name">Marrowfield and Kelton<br>Clinical Commissioning Group</p>
    </div>
  </main>
</body>
</html>
```